Business Card Design

Im looking for a business card that will market/promote myself as in independent/freelancer in the beauty industry. Im looking for something very modern, and clean looking. no specific colors just something that doesnt look cheesy, would like a very professional look

Industry/Entity Type

Business

Contact Information for Business Card

Corinne Balstrade, Hairstylist(Cut, color, blowdry, style, extensions, straightening treatments), makeup artist, red carpet, in-salon, editorial, tv, film, contact is 5307419863 cbglam@mailbrook.net, LA based

```html
<!DOCTYPE html>
<html lang="en">
<head>
<meta charset="utf-8">
<title>Corinne Balstrade — Hairstylist Business Card</title>
<link rel="stylesheet" href="https://fonts.googleapis.com/css2?family=Inter:wght@200;300;400&display=swap">
<style>
  :root {
    --canvas: #ffffff;
    --magenta: #d81b5c;
    --grey: #a7a7a7;
    --ink: #111111;
    --paper: #ffffff;
    --rule: #bdbdbd;
  }
  html, body {
    margin: 0;
    padding: 0;
    width: 1200px;
    height: 848px;
    overflow: hidden;
    background: var(--canvas);
  }
  .canvas {
    position: relative;
    width: 1200px;
    height: 848px;
    font-family: "Inter", "Helvetica Neue", Arial, sans-serif;
  }
  .card {
    position: absolute;
    top: 309px;
    width: 385px;
    height: 231px;
    box-sizing: border-box;
  }
  .card--front {
    left: 193px;
    background: var(--magenta);
    text-align: center;
  }
  .card--back {
    left: 622px;
    top: 308px;
    height: 232px;
    background: var(--paper);
    border: 1px solid var(--rule);
  }
  .identity {
    position: absolute;
    left: 0;
    right: 0;
    top: 100px;
  }
  .identity__name {
    margin: 0;
    font-size: 22px;
    line-height: 24px;
    letter-spacing: -0.04em;
    color: var(--ink);
  }
  .identity__first { font-weight: 200; }
  .identity__last { font-weight: 400; }
  .identity__role {
    margin: 0;
    font-size: 11.5px;
    font-weight: 300;
    color: var(--paper);
    letter-spacing: -0.01em;
  }
  .services {
    position: absolute;
    left: 0;
    top: 0;
  }
  .service {
    font-family: "Inter", "Helvetica Neue", Arial, sans-serif;
    font-weight: 200;
    letter-spacing: -0.03em;
  }
  .service--accent { fill: var(--magenta); }
  .service--muted { fill: var(--grey); }
  .contact {
    font-family: "Inter", "Helvetica Neue", Arial, sans-serif;
    font-weight: 300;
    font-size: 12.5px;
    fill: var(--ink);
  }
</style>
</head>
<body>
<main class="canvas">
  <section class="card card--front">
    <div class="identity">
      <h1 class="identity__name"><span class="identity__first">Corinne</span><span class="identity__last">Balstrade</span></h1>
      <p class="identity__role">Hairstylist</p>
    </div>
  </section>

  <section class="card card--back">
    <svg class="services" width="385" height="232" viewBox="0 0 385 232" xmlns="http://www.w3.org/2000/svg">
      <text class="service service--accent" x="14" y="41" font-size="24">red carpet</text>
      <text class="service service--muted" x="128" y="42" font-size="44">tv</text>
      <text class="service service--accent" x="184" y="54" font-size="38">film</text>
      <text class="service service--accent" x="293" y="52" font-size="38">style</text>
      <text class="service service--accent" x="23" y="81" font-size="24">straightening treatments</text>
      <text class="service service--accent" x="242" y="101" font-size="16">extensions</text>
      <text class="service service--muted" x="46" y="135" font-size="34">in-salon</text>
      <text class="service service--muted" x="179" y="154" font-size="24">blowdry</text>
      <text class="service service--accent" x="271" y="142" font-size="48">color</text>
      <text class="service service--accent" x="22" y="172" font-size="24">editorial</text>
      <text class="service service--muted" x="18" y="213" font-size="48">cut</text>
      <text class="service service--accent" x="106" y="193" font-size="20">makeup artist</text>
      <text class="contact" x="356" y="179" text-anchor="end">530 741 98 63</text>
      <text class="contact" x="356" y="195" text-anchor="end">cbglam@mailbrook.net</text>
      <text class="contact" x="356" y="211" text-anchor="end">LA based</text>
    </svg>
  </section>
</main>
</body>
</html>
```